Educational non-profit needs an End of the Year Flyer

We need a flyer to mail to our supporters asking for donations to our program. Crestwood Lantern Youth House runs after school programs for low-income students in Pasadena, CA. This is our end of the year mailing to supporters asking them to finish out the year with their contributions so that we can meet our budget.

Target Market(s)

Donors and supporters of organization

Industry/Entity Type

Non-Profit

Font styles to use
Serif

Colors

Designer to choose colors to be used in the design.

Requirements
Must have
• The project should fit on a 6x9" card, and be printed on front and back. It should show pictures, use the copy I have included, a space for a label address, a stamp, and the return address.
Nice to have
• eye-catching, fun

```html
<!DOCTYPE html>
<html lang="en">
<head>
<meta charset="utf-8">
<title>Crestwood Lantern Youth House – Year-End Appeal Postcard</title>
<link href="https://fonts.googleapis.com/css2?family=Poppins:ital,wght@0,400;0,500;0,600;0,700;1,500&family=Oswald:wght@300;400;500&family=Courgette&display=swap" rel="stylesheet">
<style>
  :root{
    --stage:#b86a12;
    --blue:#2b3990;
    --yellow:#f5ec1a;
    --ink:#222222;
    --grey:#555555;
    --band:#151515;
    --white:#ffffff;
  }
  *{margin:0;padding:0;box-sizing:border-box;}
  html,body{width:953px;height:1200px;overflow:hidden;background:var(--stage);}
  body{position:relative;font-family:"Poppins",sans-serif;color:var(--ink);}
  .card{position:absolute;overflow:hidden;box-shadow:0 8px 10px rgba(0,0,0,.35);}
  .card svg.art{position:absolute;left:0;top:0;}
  .front{left:107px;top:60px;width:727px;height:484px;}
  .back{left:105px;top:606px;width:733px;height:488px;}
  .abs{position:absolute;white-space:nowrap;}

  /* front */
  .org-name{left:14px;top:70px;width:150px;white-space:normal;font-weight:600;font-size:15px;line-height:1.25;color:var(--blue);text-align:center;}
  .headline-need{left:31px;top:240px;font-weight:700;font-size:28px;color:var(--blue);}
  .headline-help{left:31px;top:273px;font-size:24px;color:var(--ink);}
  .headline-year{left:31px;top:301px;font-weight:700;font-size:38px;color:var(--blue);line-height:1.1;}
  .headline-year span{font-size:22px;color:var(--ink);margin-left:8px;}
  .intro{left:31px;top:353px;font-size:11.8px;line-height:15.2px;color:var(--grey);}
  .intro b{color:var(--blue);font-weight:600;font-size:14.5px;}
  .intro i{font-weight:500;color:var(--ink);}
  .donate{left:360px;top:270px;width:120px;text-align:center;color:var(--blue);}
  .donate .script{display:block;font-family:"Courgette",cursive;font-size:27px;line-height:32px;}
  .donate .now{display:block;font-weight:700;font-size:18px;line-height:22px;}
  .web-band{left:0;top:441px;width:727px;height:43px;line-height:43px;text-align:center;background:var(--band);color:var(--white);font-size:17px;}
  .web-band strong{color:var(--yellow);font-weight:700;}

  /* back */
  .lead{left:24px;top:40px;font-size:16px;color:var(--ink);}
  .programs{left:24px;top:62px;font-weight:700;font-size:23.5px;line-height:28px;color:var(--blue);}
  .rule{left:26px;top:124px;width:146px;height:1px;background:var(--grey);}
  .members{left:26px;top:133px;font-size:9.5px;line-height:11.5px;color:var(--grey);}
  .budget-title{left:27px;top:208px;font-family:"Oswald",sans-serif;font-weight:400;font-size:20px;color:var(--white);}
  .budget-copy{left:27px;top:236px;font-family:"Oswald",sans-serif;font-weight:500;font-size:15px;line-height:19px;color:var(--yellow);}
  .join{left:24px;top:310px;font-weight:700;font-size:15.5px;color:var(--blue);}
  .join-sub{left:24px;top:328px;font-weight:500;font-size:13px;color:var(--ink);}
  .join-note{left:24px;top:347px;font-size:10.5px;color:var(--grey);}
  .contacts{left:24px;top:377px;list-style:none;font-size:11.5px;color:var(--grey);}
  .contacts li{display:flex;align-items:flex-start;line-height:16px;margin-bottom:1px;}
  .contacts li svg{width:12px;height:12px;margin-right:9px;margin-top:2px;flex:none;}
  .contacts li.tall{margin-bottom:3px;}
</style>
</head>
<body>

<section class="card front" aria-label="Postcard front">
  <svg class="art" width="727" height="484" viewBox="0 0 727 484">
    <defs>
      <linearGradient id="wall" x1="0" y1="0" x2="1" y2="1">
        <stop offset="0" stop-color="#f2f1f0"/><stop offset="1" stop-color="#e2e0de"/>
      </linearGradient>
      <linearGradient id="photoA" x1="0" y1="0" x2="0" y2="1">
        <stop offset="0" stop-color="#c9a56a"/><stop offset="1" stop-color="#6d5a4a"/>
      </linearGradient>
      <linearGradient id="photoB" x1="0" y1="0" x2="0" y2="1">
        <stop offset="0" stop-color="#2a2424"/><stop offset="1" stop-color="#b86a8a"/>
      </linearGradient>
      <linearGradient id="photoC" x1="0" y1="0" x2="0" y2="1">
        <stop offset="0" stop-color="#9c8b78"/><stop offset="1" stop-color="#5a4a44"/>
      </linearGradient>
    </defs>
    <rect role="img" aria-label="White painted brick wall texture" width="727" height="484" fill="url(#wall)"/>
    <polygon points="0,0 157,0 209,92 145,206 0,206" fill="var(--white)" stroke="#111" stroke-width="3"/>
    <polygon points="325,218 509,218 422,400" fill="var(--blue)"/>
    <polygon role="img" aria-label="Photo: a smiling girl holding a handwritten letter in a classroom" points="501,141 464,204 392,204 355,141 392,78 464,78" fill="url(#photoA)" stroke="var(--yellow)" stroke-width="6"/>
    <polygon role="img" aria-label="Photo: two young sisters hugging" points="713,91 677,154 605,154 569,91 605,28 677,28" fill="url(#photoB)" stroke="var(--yellow)" stroke-width="6"/>
    <polygon role="img" aria-label="Photo: group of program children posing in a gym with basketballs" points="721,290 659,414 533,414 471,290 533,166 659,166" fill="url(#photoC)" stroke="var(--yellow)" stroke-width="7"/>
    <polygon points="493,301 457,364 384,364 347,301 384,238 457,238" fill="var(--white)" stroke="var(--yellow)" stroke-width="6"/>
  </svg>

  <div class="abs org-name">Crestwood Lantern Youth House</div>

  <h1 class="abs headline-need">WE NEED</h1>
  <p class="abs headline-help">your help to finish out</p>
  <p class="abs headline-year">2018<span>STRONG!</span></p>
  <p class="abs intro">We have had a wonderful <b>25th year</b> of serving<br>the children and families of Pasadena here at<br><i>Crestwood Lantern Youth House</i><br>with high quality after school programs.</p>

  <p class="abs donate"><span class="script">Donate</span><span class="now">NOW!</span></p>

  <p class="abs web-band">JUST LOOK FOR THE LINK ON OUR WEBSITE <strong>- WWW.CRESTWOODLANTERN.ORG.</strong></p>
</section>

<section class="card back" aria-label="Postcard back">
  <svg class="art" width="733" height="488" viewBox="0 0 733 488">
    <defs>
      <linearGradient id="wall2" x1="0" y1="0" x2="1" y2="1">
        <stop offset="0" stop-color="#f2f1f0"/><stop offset="1" stop-color="#e2e0de"/>
      </linearGradient>
    </defs>
    <rect role="img" aria-label="White painted brick wall texture" width="733" height="488" fill="url(#wall2)"/>
    <rect x="0" y="194" width="280" height="101" fill="var(--blue)"/>
    <polygon points="379,0 434,0 266,248 437,488 382,488 243,248" fill="var(--yellow)"/>
    <polygon points="434,0 733,0 733,488 437,488 266,248" fill="var(--white)"/>
    <rect class="stamp" x="581" y="52" width="101" height="100" fill="none" stroke="#555" stroke-width="1.2"/>
    <g class="address-lines" stroke="#666" stroke-width="1.2" stroke-dasharray="2 2">
      <line x1="446" y1="234" x2="683" y2="234"/>
      <line x1="446" y1="262" x2="683" y2="262"/>
      <line x1="446" y1="288" x2="683" y2="288"/>
      <line x1="446" y1="318" x2="683" y2="318"/>
    </g>
  </svg>

  <p class="abs lead">Educational and community-building</p>
  <h2 class="abs programs">Programs for Children,<br>Youth and Families</h2>
  <div class="abs rule"></div>
  <p class="abs members">Hundreds and hundreds of students<br>have been a part of the Lantern Kids Club family.</p>

  <h3 class="abs budget-title">OUR ANNUAL BUDGET</h3>
  <p class="abs budget-copy">Is $275,000 and we count on<br>$100,000 from individual donors.</p>

  <h3 class="abs join">WILL YOU JOIN WITH US FOR</h3>
  <p class="abs join-sub">An end of the year contribution?</p>
  <p class="abs join-note">Remember, you can give online through Donaloop Online.</p>

  <ul class="abs contacts">
    <li><svg viewBox="0 0 12 12"><circle cx="6" cy="6" r="5" fill="none" stroke="#2b3990" stroke-width="1.2"/><path d="M1 6h10M6 1c-2.5 3-2.5 7 0 10M6 1c2.5 3 2.5 7 0 10" fill="none" stroke="#2b3990" stroke-width="1"/></svg>www.crestwoodlantern.org</li>
    <li><svg viewBox="0 0 12 12"><rect x="3" y="2" width="6" height="8" fill="#2b3990"/></svg>Crestwood Lantern Youth House</li>
    <li><svg viewBox="0 0 12 12"><rect x="1" y="2.5" width="10" height="7" fill="#2b3990"/><path d="M1 2.5l5 4 5-4" fill="none" stroke="#fff" stroke-width="1"/></svg>hello@crestwoodlantern.org</li>
    <li class="tall"><svg viewBox="0 0 12 12"><path d="M6 11.5C3 7.5 2 6 2 4.2a4 4 0 0 1 8 0C10 6 9 7.5 6 11.5z" fill="#2b3990"/><circle cx="6" cy="4.3" r="1.5" fill="#fff"/></svg><span>Crestwood Lantern Youth House<br>418 N. Marlowe Ave. Pasadena, CA&nbsp; 91104</span></li>
    <li><svg viewBox="0 0 12 12"><path d="M2.5 1l2 .3 1 2.6-1.4 1.1a7 7 0 0 0 3 3l1.1-1.4 2.6 1 .2 2c0 .6-.5 1.2-1.2 1.2A9.8 9.8 0 0 1 1.2 2.2c0-.7.6-1.2 1.3-1.2z" fill="#2b3990"/></svg>(626) 555-0147</li>
  </ul>
</section>

</body>
</html>
```